Visitenkarten-Design für Stillberaterin
Zielgruppe
Ich bin Stillberaterin ZMVQA, d. h. ich berate Mütter bei Stillschwierigkeiten. Meine Zielgruppe sind junge Familien, die sich vorab über das Stillen Ihres Kindes informieren möchten, Stillschwierigkeiten (z. B. Schmerzen, schlechte Gewichtszunahme usw.) haben oder Fragen rund ums Stillen haben (Medikamente, Stillen in besonderen Situationen...). Weiterhin biete ich Kurse für den Beikoststart oder zum Abstillen an.
Aufgabenstellung
Auf meiner Visitenkarte sollte mein Logo sowie alle Kontaktdaten klar und deutlich erkennbar sein. Die Farben sind dem Logo anzupassen. Die Schriftarten, die im Logo verwendet werden sind: Be Bright und Apple Tree

```html
<!DOCTYPE html>
<html lang="de">
<head>
<meta charset="utf-8">
<title>Visitenkarte Stillzeit-Nest</title>
<link href="https://fonts.googleapis.com/css2?family=Allura&family=Open+Sans:wght@400;600&display=swap" rel="stylesheet">
<style>
  :root {
    --pink: #e5549f;
    --pink-soft: #f7c6df;
    --pink-pale: #fdeef5;
    --ink: #2b2b2b;
    --rule: #8a8a8a;
    --card: #ffffff;
    --backdrop: #e9e9ec;
  }
  * { box-sizing: border-box; margin: 0; padding: 0; }
  html, body { width: 1200px; height: 900px; overflow: hidden; }
  body {
    background: var(--backdrop);
    font-family: "Open Sans", Arial, sans-serif;
    color: var(--ink);
    position: relative;
  }
  .card {
    position: absolute;
    top: 275px;
    width: 540px;
    height: 350px;
    background: var(--card);
    box-shadow: 0 4px 18px rgba(0,0,0,0.12);
    overflow: hidden;
  }
  .card--contact { left: 40px; }
  .card--front { left: 620px; }

  /* contact side */
  .brand-block {
    position: absolute;
    left: 0; top: 0;
    width: 190px; height: 350px;
    display: flex; flex-direction: column;
    align-items: center; justify-content: center;
    gap: 10px;
  }
  .brand-dot {
    width: 44px; height: 44px;
    border-radius: 50%;
    background: var(--pink-soft);
  }
  .brand-name {
    font-weight: 600;
    font-size: 18px;
    color: var(--pink);
  }
  .divider {
    position: absolute;
    left: 190px; top: 50px;
    width: 1px; height: 250px;
    background: var(--rule);
  }
  .contact {
    position: absolute;
    left: 220px; top: 60px; right: 20px;
  }
  .person-name {
    font-family: "Allura", cursive;
    font-size: 42px;
    line-height: 1;
    color: var(--pink);
  }
  .person-role {
    font-size: 10.5px;
    line-height: 1.35;
    margin-top: 6px;
  }
  .address {
    font-size: 16px;
    line-height: 1.35;
    margin-top: 16px;
  }
  .channels { list-style: none; margin-top: 12px; }
  .channels li {
    display: flex; align-items: center; gap: 8px;
    font-size: 16px; line-height: 1.5;
  }
  .channels svg { width: 13px; height: 13px; flex: none; }

  /* front side */
  .motif {
    position: absolute;
    left: 0; top: 0;
    width: 250px; height: 350px;
    background: linear-gradient(135deg, var(--pink-pale) 0%, var(--pink-soft) 100%);
  }
  .front-brand {
    position: absolute;
    left: 270px; top: 120px; right: 20px;
    text-align: center;
  }
  .front-brand .brand-name { font-size: 30px; }
  .tagline {
    font-size: 13px;
    color: var(--pink);
    margin-top: 6px;
  }
  .web {
    position: absolute;
    left: 270px; right: 20px; bottom: 36px;
    display: flex; align-items: center; justify-content: center; gap: 12px;
    font-size: 13px; color: var(--pink);
  }
  .web-rule { width: 40px; height: 1px; background: var(--pink); }
</style>
</head>
<body>
  <section class="card card--contact">
    <div class="brand-block">
      <span class="brand-dot"></span>
      <span class="brand-name">Stillzeit-Nest</span>
    </div>
    <div class="divider"></div>
    <div class="contact">
      <h1 class="person-name">Jorunda Tulrik</h1>
      <p class="person-role">Fachkinderkrankenschwester,<br>Still- &amp; Laktationsberaterin ZMVQA</p>
      <p class="address">Am Lindenhang 4<br>93099 Musterbach</p>
      <ul class="channels">
        <li>
          <svg viewBox="0 0 16 16" aria-hidden="true"><path fill="#e5549f" d="M3.6 1.5l2.2 2.6-1.3 1.6c.8 2 2.3 3.6 4.3 4.4l1.6-1.3 2.6 2.2-1.4 2.2C6.8 13 3 9.2 1.4 3z"/></svg>
          09401 2718305
        </li>
        <li>
          <svg viewBox="0 0 16 16" aria-hidden="true"><rect x="1" y="3" width="14" height="10" fill="#e5549f"/><path d="M1 3l7 6 7-6" fill="none" stroke="#fff" stroke-width="1.3"/></svg>
          jorunda@stillzeit-nest.de
        </li>
        <li>
          <svg viewBox="0 0 16 16" aria-hidden="true"><circle cx="8" cy="8" r="6.5" fill="none" stroke="#e5549f" stroke-width="1.5"/><path d="M1.5 8h13M8 1.5c-3 3.5-3 9.5 0 13M8 1.5c3 3.5 3 9.5 0 13" fill="none" stroke="#e5549f" stroke-width="1.2"/></svg>
          www.stillzeit-nest.de
        </li>
      </ul>
    </div>
  </section>

  <section class="card card--front">
    <div class="motif" role="img" aria-label="Pinke Linienzeichnung einer stillenden Mutter mit Herzmotiv"></div>
    <div class="front-brand">
      <div class="brand-name">Stillzeit-Nest</div>
      <p class="tagline">Stillberatung für Regensburg</p>
    </div>
    <div class="web">
      <span class="web-rule"></span>
      www.stillzeit-nest.de
      <span class="web-rule"></span>
    </div>
  </section>
</body>
</html>
```